Business Card Design needed for logo design project

Our company needs a Business Card Design. Please refer to our original project in the link above.

Industry/Entity Type

Business

```html
<!DOCTYPE html>
<html lang="en">
<head>
<meta charset="UTF-8">
<title>nuvelo — Business Card</title>
<link rel="stylesheet" href="https://fonts.googleapis.com/css2?family=Arimo:wght@400&display=swap">
<style>
  :root {
    --backdrop: #1b1b1c;
    --card-face: #2c2c2d;
    --card-face-dark: #242425;
    --pattern-tone: #1f1f20;
    --brand-grey: #8d8d8f;
    --text-grey: #8a8a8c;
    --text-muted: #6e6e70;
    --rule-grey: #7a7a7c;
  }
  * { margin: 0; padding: 0; box-sizing: border-box; }
  html, body {
    width: 1200px;
    height: 900px;
    overflow: hidden;
    background: var(--backdrop);
    font-family: "Arimo", Arial, sans-serif;
  }
  .stage {
    position: relative;
    width: 1200px;
    height: 900px;
  }
  .card {
    position: absolute;
    width: 560px;
    height: 320px;
    border-radius: 26px;
    overflow: hidden;
    background: var(--card-face);
  }
  /* Back of card */
  .card-back {
    left: 560px;
    top: 110px;
    background: var(--card-face-dark);
  }
  .card-back .pattern-field {
    position: absolute;
    inset: 0;
    background: linear-gradient(120deg, var(--pattern-tone) 0%, #262627 55%, var(--pattern-tone) 100%);
  }
  .card-back .wordmark {
    position: absolute;
    right: 42px;
    bottom: 52px;
    font-size: 40px;
    letter-spacing: 1px;
    color: var(--brand-grey);
  }
  /* Front of card */
  .card-front {
    left: 80px;
    top: 470px;
  }
  .card-front .wordmark {
    position: absolute;
    left: 44px;
    bottom: 48px;
    font-size: 68px;
    letter-spacing: 1px;
    color: var(--brand-grey);
  }
  .contact-block {
    position: absolute;
    left: 280px;
    top: 44px;
    color: var(--text-grey);
  }
  .person-name {
    font-size: 19px;
    color: var(--text-grey);
  }
  .person-title {
    font-size: 12px;
    color: var(--text-muted);
    margin-top: 3px;
  }
  .address {
    font-size: 13px;
    line-height: 1.4;
    margin-top: 26px;
    color: var(--text-muted);
  }
  .reach {
    margin-top: 24px;
    padding-left: 16px;
    border-left: 1px solid var(--rule-grey);
    font-size: 13px;
    line-height: 1.5;
    color: var(--text-muted);
  }
</style>
</head>
<body>
  <main class="stage">
    <section class="card card-back" aria-label="Business card back">
      <div class="pattern-field" role="img" aria-label="Tone-on-tone repeating brand name pattern across the card"></div>
      <div class="wordmark">nuvelo</div>
    </section>

    <section class="card card-front" aria-label="Business card front">
      <div class="contact-block">
        <p class="person-name">Daniel Reyes</p>
        <p class="person-title">title here</p>
        <p class="address">2715 Harbor Crest Avenue<br>Portland, OR 97205</p>
        <p class="reach">+1 555 018 2947<br>hello@nuvelo.com<br>www.nuvelo.com</p>
      </div>
      <div class="wordmark">nuvelo</div>
    </section>
  </main>
</body>
</html>
```